Attorney Recruiting company needs brochure

Brief Harbor is a company that recruits attorneys for law firms and corporations. We want a brochure that makes the law firms and corporation want to retain us to recruit attorneys when they are hiring. We identify experienced well qualified attorneys. We provide them for direct hire (also knows as permanent placement) and for temporary contract hourly work. We want our colors included: red, black and white. It has to convey professionalism and experience. You can find lots of information about who we are and what we do on our website. www.briefharbor-example.com. The brochure should be in traditional conservative font. Should be easy to read. Attorneys tend to scan brochures to see what we do, they will need read it word for word, so we don't need lots of paragraphs and extraneous text. The brochure should outline easily the services we provide which are very specific. They are outlined on home page of website. You should also include our logo which I will attach in several formats.

Target Market(s)

Attorneys and executives

Industry/Entity Type

Conservative

Requirements
Must have
• logo
colors described above

```html
<!DOCTYPE html>
<html lang="en">
<head>
<meta charset="utf-8">
<title>Brief Harbor — Attorney Recruitment &amp; Placement</title>
<link rel="stylesheet" href="https://fonts.googleapis.com/css2?family=Arimo:wght@700&family=Cinzel:wght@600&display=swap">
<style>
  :root {
    --brand-red: #a8000f;
    --ink: #1a1a1a;
    --paper: #ffffff;
    --photo-sky: #9fd0e6;
    --photo-mid: #4e8297;
    --photo-deep: #2b4652;
  }
  html, body {
    margin: 0;
    padding: 0;
    overflow: hidden;
    background: var(--paper);
  }
  .brochure-cover {
    position: relative;
    width: 848px;
    height: 1200px;
    overflow: hidden;
    background: var(--paper);
  }
  .brand {
    position: absolute;
    left: 52px;
    top: 62px;
    display: flex;
    align-items: center;
    gap: 16px;
  }
  .brand-square {
    width: 46px;
    height: 46px;
    background: var(--brand-red);
  }
  .brand-text {
    display: flex;
    flex-direction: column;
  }
  .brand-name {
    font-family: "Cinzel", "Times New Roman", serif;
    font-weight: 600;
    font-size: 38px;
    line-height: 1;
    color: var(--ink);
    letter-spacing: 0.5px;
  }
  .brand-tagline {
    margin-top: 8px;
    font-family: "Cinzel", "Times New Roman", serif;
    font-weight: 600;
    font-size: 12.5px;
    letter-spacing: 1px;
    color: var(--ink);
    border-top: 1.5px solid var(--brand-red);
    padding-top: 5px;
  }
  .service-statement {
    position: absolute;
    left: 131px;
    top: 298px;
    margin: 0;
    font-family: "Arimo", Arial, sans-serif;
    font-weight: 700;
    font-size: 24.5px;
    line-height: 35px;
    letter-spacing: 0.3px;
    color: var(--brand-red);
    text-transform: uppercase;
  }
  .color-block {
    position: absolute;
    left: 0;
    top: 751px;
    width: 339px;
    height: 449px;
    background: var(--brand-red);
  }
  .photo-area {
    position: absolute;
    left: 339px;
    top: 751px;
    width: 509px;
    height: 449px;
    background:
      radial-gradient(ellipse at 72% 60%, rgba(120,120,120,0.55) 0%, rgba(120,120,120,0) 45%),
      linear-gradient(180deg, var(--photo-sky) 0%, var(--photo-mid) 55%, var(--photo-deep) 100%);
  }
</style>
</head>
<body>
  <main class="brochure-cover">
    <header class="brand">
      <div class="brand-square"></div>
      <div class="brand-text">
        <span class="brand-name">Brief Harbor</span>
        <span class="brand-tagline">Attorney Recruitment &amp; Placement</span>
      </div>
    </header>

    <p class="service-statement">
      We are the experts in attorney<br>
      recruitment and placement in<br>
      Central Florida. We specialize<br>
      in full service recruitment<br>
      of attorneys for direct hire<br>
      and temporary placement.<br>
      Our placement services are<br>
      offered to attorneys, law<br>
      firms and companies seeking<br>
      in-house counsel.
    </p>

    <div class="color-block"></div>
    <div class="photo-area" role="img" aria-label="Photo of a professional in a grey three-piece suit carrying a jacket over his shoulder, walking through a bright glass-walled office lobby"></div>
  </main>
</body>
</html>
```